Consulting firm needs elegant, modern designs

Business card design - I have a logo which has previously been developed for Q-Pathways - I will attach. I will also attach specifications for the size of the business card.

We also need a logo design for our leadership consulting product - Form in Guidance - we focus on improving workplace health by educating leaders and learning professionals about how the physical and emotional affects performance and engagement. I have some example logos and ideas which I will attach - these have attempted to bring in the body but I do not like the font (see www.formingguidance-example.com for preferred font). Idea is to please have a 'body' visible somehow in the word Leadership, ensuring that this conveys flexibility and agility. Colors which I prefer are deep purple OR turquoise, together with silver. COLORS below are for LOGO design.

Target Market(s)

For the business card, it should be more masculine. The logo which will be attached should be neutralized into dark blue shades and silver. The business card Q-Pathways is focused on business transformation - organizations who would require a consultant to help them enter new markets, for example.

Industry/Entity Type

Leadership

Contact Information for Business Card

Content:
Q-Pathways
Lindenkade 27
4921KP, Breda, The Netherlands
maurits@Q-Pathways.example
www.Q-Pathways.example

Colors for business card should be conservative and slightly more masculine. Use the Q-Pathways logo but change the colors to blue or shades of gray/black.

Dimensions for cut
85 x 55 mm
1004 x 650 pixels
Full document size
88 x 58 mm
1040 x 685 pixels
For the best result, you need to design the full document size including the bleed

Logo Text

Form in Guidance

Font styles to use
Serif
Sans Serif

Colors
876aae
333333
959595

Requirements
Must have
• Professional, modern and unique business card design
• Professional, elegant, and modern logo design - with creative thinking
Should not have
• Too many colors

```html
<!DOCTYPE html>
<html lang="en">
<head>
<meta charset="utf-8">
<title>Q-Pathways Business Card</title>
<link href="https://fonts.googleapis.com/css2?family=Open+Sans:wght@400;600;700&display=swap" rel="stylesheet">
<style>
  :root {
    --brand-blue: #0b2a9c;
    --ink-blue: #1a2e8f;
    --ink-dark: #2b2b2b;
    --rule-grey: #b9b9b9;
    --card-white: #ffffff;
    --backdrop: #e6e6e8;
  }
  * { box-sizing: border-box; margin: 0; padding: 0; }
  html, body {
    width: 1200px; height: 900px; overflow: hidden;
    background: var(--backdrop);
    font-family: "Open Sans", Arial, sans-serif;
  }
  .sheet {
    position: relative; width: 1200px; height: 900px;
    display: flex; align-items: center; justify-content: center; gap: 40px;
  }
  .card {
    width: 520px; height: 336px; position: relative;
    box-shadow: 0 6px 18px rgba(0,0,0,0.18);
  }
  .card--front { background: var(--card-white); }
  .card--back {
    background: var(--brand-blue);
    display: flex; align-items: center; justify-content: center;
  }
  .brand {
    display: flex; align-items: center; gap: 10px;
    white-space: nowrap;
  }
  .brand__dot {
    width: 36px; height: 36px; border-radius: 50%;
    background: var(--brand-blue); flex: none;
  }
  .brand__name {
    font-weight: 600; font-size: 28px; letter-spacing: 0.2px;
    color: var(--brand-blue); line-height: 1;
  }
  .card--back .brand { gap: 12px; }
  .card--back .brand__dot { width: 58px; height: 58px; background: var(--card-white); }
  .card--back .brand__name { color: var(--card-white); font-size: 42px; }
  .card--front .brand {
    position: absolute; left: 42px; top: 50%; transform: translateY(-50%);
  }
  .divider {
    position: absolute; left: 296px; top: 34px; bottom: 34px; width: 1px;
    background: linear-gradient(to bottom, rgba(185,185,185,0), var(--rule-grey) 30%, var(--rule-grey) 70%, rgba(185,185,185,0));
  }
  .details {
    position: absolute; left: 312px; top: 80px;
    font-size: 12px; line-height: 1.35; color: var(--ink-dark);
    white-space: nowrap;
  }
  .details__name, .details__company {
    font-weight: 700; color: var(--ink-blue);
  }
  .details__name { font-size: 13px; }
  .details__role { margin-bottom: 10px; }
  .contact { display: flex; align-items: center; gap: 6px; }
  .contact svg { width: 10px; height: 10px; flex: none; }
  .contact-list { margin-bottom: 10px; }
</style>
</head>
<body>
<main class="sheet">
  <section class="card card--front" aria-label="Business card front">
    <div class="brand">
      <span class="brand__dot"></span>
      <span class="brand__name">Q-Pathways</span>
    </div>
    <div class="divider"></div>
    <div class="details">
      <p class="details__name">Dorian Vale</p>
      <p class="details__role">Managing Director</p>
      <div class="contact-list">
        <p class="contact">
          <svg viewBox="0 0 12 12" aria-hidden="true"><rect x="0.5" y="2" width="11" height="8" fill="#1a2e8f"/><path d="M0.5 2 L6 6.5 L11.5 2" stroke="#fff" stroke-width="1" fill="none"/></svg>
          maurits@Q-Pathways.example
        </p>
        <p class="contact">
          <svg viewBox="0 0 12 12" aria-hidden="true"><circle cx="6" cy="6" r="5.5" fill="#1a2e8f"/><path d="M0.5 6 H11.5 M6 0.5 C3 3 3 9 6 11.5 M6 0.5 C9 3 9 9 6 11.5" stroke="#fff" stroke-width="0.8" fill="none"/></svg>
          www.Q-Pathways.example
        </p>
      </div>
      <p class="details__company">Q-Pathways</p>
      <p>Lindenkade 27</p>
      <p>4921KP, Breda, The Netherlands</p>
    </div>
  </section>
  <section class="card card--back" aria-label="Business card back">
    <div class="brand">
      <span class="brand__dot"></span>
      <span class="brand__name">Q-Pathways</span>
    </div>
  </section>
</main>
</body>
</html>
```